Wordpress Web Design for Coach/Consultant

I need a website for my business consulting and life coaching website.
Fully responsive website built on the WordPress self-hosted content management system
CMS Installation
Fully customized graphics and design
Customized slideshow presentation slides
Up to ten main navigation content tabs
SEO optimization
Contact form configuration
Customized favicon and social media icons
Photo gallery creation
Customized portfolio
Social media integration
Blog integration
Content sharing buttons
Subscription signup integration

Target Market(s)

Women Entrepreneurs

Industry/Entity Type

Life Coaching

Number of Pages Required

5+ page

Font styles to use
Sans Serif
Decorative

Colors
ec1f27
ffffff
000000

Requirements
Must have
• Fully responsive website built on the WordPress self-hosted content management system
• CMS Installation
• Fully customized graphics and design
• Customized slideshow presentation slides
• Up to ten main navigation content tabs
• SEO optimization
• Contact form configuration
• Customized favicon and social media icons
• Photo gallery creation
• Customized portfolio
• Social media integration
• Blog integration
• Content sharing buttons
• Subscription signup integration
Nice to have
• Here are a few sample websites to take a look at:
• www.corvalyndetrie.com

```html
<!DOCTYPE html>
<html lang="en">
<head>
<meta charset="utf-8">
<title>Marlowe – Business Consulting &amp; Life Coaching</title>
<link href="https://fonts.googleapis.com/css2?family=Open+Sans:wght@400;600;700&family=Raleway:wght@400;600;700&display=swap" rel="stylesheet">
<style>
:root{
  --navy:#1c3a6b;
  --navy-deep:#14294f;
  --blue:#2a78d4;
  --blue-link:#2665b8;
  --ink:#333333;
  --muted:#777777;
  --grey-band:#e9e9e9;
  --white:#ffffff;
  --line:#dddddd;
}
*{margin:0;padding:0;box-sizing:border-box}
html,body{width:1200px;height:3020px;overflow:hidden;background:var(--white)}
body{font-family:"Open Sans",Arial,sans-serif;color:var(--ink)}
.page{position:relative;width:1200px;height:3020px}
.wrap{width:940px;margin:0 auto;position:relative}

/* Header + hero */
.top{background:linear-gradient(180deg,var(--navy-deep) 0%,var(--navy) 100%);height:760px;color:var(--white)}
.nav{height:84px;display:flex;align-items:center;justify-content:space-between}
.logo{font-family:"Raleway",sans-serif;font-size:44px;font-weight:600;color:var(--white);letter-spacing:1px}
.menu{display:flex;list-style:none;align-self:flex-start}
.menu li{font-size:12px;font-weight:600;padding:14px 12px;letter-spacing:.5px}
.menu li.active{background:var(--blue)}
.hero{height:380px;position:relative;display:flex;background:#eef2f7;overflow:hidden}
.hero-photo{width:52%;height:100%;background:linear-gradient(120deg,#3b4f6e 0%,#6d7f99 55%,#c9d3df 100%)}
.hero-copy{flex:1;display:flex;flex-direction:column;justify-content:center;padding:0 40px;background:linear-gradient(90deg,#c9d3df 0%,#f3f5f8 40%)}
.hero-copy h1{font-family:"Raleway",sans-serif;font-weight:400;font-size:30px;line-height:1.3;color:var(--navy)}
.btn{display:inline-block;background:var(--blue);color:var(--white);font-size:12px;font-weight:700;padding:10px 22px;letter-spacing:1px;margin-top:22px;width:max-content}
.dots{position:absolute;right:26px;bottom:18px;display:flex;gap:7px}
.dots span{width:10px;height:10px;border-radius:50%;background:var(--white);opacity:.6}
.dots span:first-child{opacity:1;background:var(--navy)}

.newsletter{text-align:center;padding-top:56px}
.newsletter h2{font-family:"Raleway",sans-serif;font-size:28px;font-weight:600}
.newsletter p{font-size:12px;line-height:1.6;opacity:.85;width:760px;margin:14px auto 24px}
.signup{display:flex;gap:16px}
.field{flex:1;height:40px;border:1px solid rgba(255,255,255,.35);background:rgba(255,255,255,.06);font-size:12px;padding:0 14px;display:flex;align-items:center;color:rgba(255,255,255,.7)}
.signup .btn{margin:0;height:40px;display:flex;align-items:center;padding:0 30px}

/* Blogs */
.blogs{padding-top:50px;height:1180px}
.section-title{text-align:center;font-family:"Raleway",sans-serif;font-weight:700;font-size:24px;letter-spacing:2px;color:#222;margin-bottom:36px}
.cards{display:grid;grid-template-columns:460px 460px;gap:34px 20px}
.card-photo{height:290px}
.card-body{display:flex;gap:16px;padding-top:0}
.date{width:66px;height:84px;background:var(--blue);color:var(--white);text-align:center;font-size:12px;font-weight:700;line-height:1.35;padding-top:12px;margin-top:-30px;flex-shrink:0}
.card-body h3{font-size:17px;line-height:1.35;color:var(--blue-link);font-weight:700;padding-top:12px}
.card-text{font-size:12px;line-height:1.65;color:var(--muted);margin-top:10px}
.card-text b{color:var(--blue-link)}
.pager{display:flex;justify-content:center;gap:8px;margin-top:40px}

/* Gallery */
.gallery{background:var(--grey-band);height:860px;padding-top:48px}
.stage{height:610px;position:relative;background:linear-gradient(135deg,#54627a 0%,#a7b3c4 45%,#e2e6ec 70%,#7d8aa0 100%)}
.caption{position:absolute;left:330px;top:250px;width:290px;background:rgba(20,30,45,.85);color:var(--white);font-size:15px;line-height:1.5;padding:20px}
.thumbs{display:flex;gap:14px;justify-content:center;align-items:center;margin-top:-64px;position:relative}
.thumb{width:150px;height:110px;border:3px solid var(--white)}
.arrow{width:26px;height:26px}

/* Footer */
.footer{padding-top:40px}
.footer .wrap{display:grid;grid-template-columns:300px 200px 230px 210px}
.footer .logo{color:var(--blue);font-size:30px}
.footer small{display:block;font-size:11px;color:var(--muted);margin:8px 0 14px}
.social{display:flex;gap:6px}
.social span{width:22px;height:22px;border-radius:50%;background:var(--blue)}
.footer h4{font-size:12px;font-weight:700;letter-spacing:1px;margin-bottom:10px;color:#222}
.footer ul{list-style:none;font-size:11px;line-height:1.75;color:var(--muted)}
.footer p{font-size:11px;line-height:1.7;color:var(--muted)}
</style>
</head>
<body>
<div class="page">

<header class="top">
  <div class="wrap">
    <nav class="nav">
      <div class="logo">Marlowe</div>
      <ul class="menu">
        <li class="active">HOME</li><li>ABOUT</li><li>CLIENTS</li><li>TRAINING</li><li>CASE STUDIES</li><li>GALLERY</li><li>BLOG</li><li>CONTACT</li>
      </ul>
    </nav>
    <section class="hero">
      <div class="hero-photo" role="img" aria-label="Photo of a team of business consultants in an office"></div>
      <div class="hero-copy">
        <h1>Business Consulting &amp; life<br>Coaching Consultant</h1>
        <span class="btn">GET STARTED</span>
      </div>
      <div class="dots"><span></span><span></span><span></span><span></span></div>
    </section>
    <section class="newsletter">
      <h2>Sign Up For Newsletter</h2>
      <p>Join our mailing list for fresh ideas on business growth and personal coaching. Each month we share practical tips, upcoming workshops and stories from women who built thriving companies with clear goals and steady habits.</p>
      <div class="signup">
        <div class="field">Enter Your Name</div>
        <div class="field">Enter Your Email Address</div>
        <span class="btn">SUBSCRIBE</span>
      </div>
    </section>
  </div>
</header>

<section class="blogs">
  <div class="wrap">
    <h2 class="section-title">LATEST BLOGS</h2>
    <div class="cards">
      <article class="card">
        <div class="card-photo" role="img" aria-label="Photo of a hand touching a glowing digital network" style="background:linear-gradient(135deg,#0c2f5c,#1f6bb5 60%,#0a2240)"></div>
        <div class="card-body"><div class="date">OCT<br>4th<br>2015</div><h3>Neque porro quisquam est qui dolorem ipsum quia dolor sit amet, consectetur, adipisci velit..</h3></div>
        <p class="card-text">Small steps add up to big change. Learn how to set weekly targets, track progress and stay motivated while your business grows faster than you planned. <b>Read More</b></p>
      </article>
      <article class="card">
        <div class="card-photo" role="img" aria-label="Photo of business partners shaking hands at a desk" style="background:linear-gradient(135deg,#d7dde6,#8d9bb0 55%,#3e4c63)"></div>
        <div class="card-body"><div class="date">OCT<br>4th<br>2015</div><h3>Neque porro quisquam est qui dolorem ipsum quia dolor sit amet, consectetur, adipisci velit..</h3></div>
        <p class="card-text">Strong partnerships start with honest conversations. Here are five questions to ask before you sign any agreement with a new client or supplier. <b>Read More</b></p>
      </article>
      <article class="card">
        <div class="card-photo" role="img" aria-label="Photo of a team meeting around a table" style="background:linear-gradient(135deg,#b9a896,#e4ddd4 50%,#7b8798)"></div>
        <div class="card-body"><div class="date">OCT<br>4th<br>2015</div><h3>Neque porro quisquam est qui dolorem ipsum quia dolor sit amet, consectetur, adipisci velit..</h3></div>
        <p class="card-text">Great meetings leave everyone clear on the next move. Try this simple agenda format to keep your team focused and your decisions moving forward. <b>Read More</b></p>
      </article>
      <article class="card">
        <div class="card-photo" role="img" aria-label="Photo of colleagues working at a desk seen from above" style="background:linear-gradient(135deg,#eef0f3,#a9b1bd 55%,#5a6475)"></div>
        <div class="card-body"><div class="date">OCT<br>4th<br>2015</div><h3>Neque porro quisquam est qui dolorem ipsum quia dolor sit amet, consectetur, adipisci velit..</h3></div>
        <p class="card-text">Balance is not a luxury for founders. Discover daily routines that protect your energy, sharpen your thinking and keep life outside work rewarding. <b>Read More</b></p>
      </article>
    </div>
    <div class="pager">
      <svg width="24" height="24" viewBox="0 0 24 24"><circle cx="12" cy="12" r="12" fill="#222"/><path d="M14 7l-5 5 5 5" stroke="#fff" stroke-width="2" fill="none"/></svg>
      <svg width="24" height="24" viewBox="0 0 24 24"><circle cx="12" cy="12" r="12" fill="#222"/><path d="M10 7l5 5-5 5" stroke="#fff" stroke-width="2" fill="none"/></svg>
    </div>
  </div>
</section>

<section class="gallery">
  <div class="wrap">
    <h2 class="section-title">GALLERY</h2>
    <div class="stage" role="img" aria-label="Photo of a team collaborating over documents and a laptop, seen from above">
      <div class="caption">Neque porro quisquam est qui dolorem ipsum quia dolor sit amet</div>
    </div>
    <div class="thumbs">
      <svg class="arrow" viewBox="0 0 24 24"><circle cx="12" cy="12" r="12" fill="#222"/><path d="M14 7l-5 5 5 5" stroke="#fff" stroke-width="2" fill="none"/></svg>
      <div class="thumb" role="img" aria-label="Thumbnail of a business meeting" style="background:linear-gradient(135deg,#6b7a92,#c5ccd7)"></div>
      <div class="thumb" role="img" aria-label="Thumbnail of a presentation" style="background:linear-gradient(135deg,#8a98ad,#e0e4ea)"></div>
      <div class="thumb" role="img" aria-label="Thumbnail of a team at work" style="background:linear-gradient(135deg,#4d5c74,#a8b3c3)"></div>
      <div class="thumb" role="img" aria-label="Thumbnail of an office discussion" style="background:linear-gradient(135deg,#9aa5b5,#eceef2)"></div>
      <div class="thumb" role="img" aria-label="Thumbnail of a consultant at a desk" style="background:linear-gradient(135deg,#5e6b80,#c0c8d4)"></div>
      <svg class="arrow" viewBox="0 0 24 24"><circle cx="12" cy="12" r="12" fill="#222"/><path d="M10 7l5 5-5 5" stroke="#fff" stroke-width="2" fill="none"/></svg>
    </div>
  </div>
</section>

<footer class="footer">
  <div class="wrap">
    <div>
      <div class="logo">Marlowe</div>
      <small>© 2015 Marlowe. All Rights reserved.</small>
      <div class="social"><span></span><span></span><span></span><span></span><span></span><span></span></div>
    </div>
    <div>
      <h4>QUICK LINKS</h4>
      <ul><li>Home</li><li>About</li><li>Clients</li><li>Training</li><li>Case Studies</li><li>Gallery</li><li>Blog</li><li>Contact</li></ul>
    </div>
    <div>
      <h4>ABOUT US</h4>
      <p>We guide women entrepreneurs through every stage of growth, pairing clear business strategy with personal coaching so results last and life stays in balance.</p>
    </div>
    <div>
      <h4>CONTACT US</h4>
      <p>Marlowe Consulting<br>27 Larkspur Lane, Suite 4<br>Fairhaven, OR 97420<br>Phone: +1 555 014 2290<br>E-mail: hello@marloweconsulting.example</p>
    </div>
  </div>
</footer>

</div>
</body>
</html>
```